I need a movie poster design for a short film.

The poster should have a BLUE handball with a old school headband around the top like a person would wear. I was thinking a blue background but ill leave that open. Can you also put the title Quiet Ferns on the poster.

its a racquetball, all blue ball, solid blue no groves, clean looking, sharp poster, thanks

white headband with, blue and red strip.

```html
<!DOCTYPE html>
<html lang="en">
<head>
<meta charset="utf-8">
<title>Quiet Ferns — Poster</title>
<link rel="stylesheet" href="https://fonts.googleapis.com/css2?family=Montserrat:wght@100;200;500;600&family=Raleway:wght@300&family=Arimo:wght@700&display=swap">
<style>
  :root {
    --wall-light: #ece5da;
    --wall-mid: #ddd3c5;
    --wall-edge: #c9bcab;
    --floor-light: #c9a47c;
    --floor-mid: #b58c62;
    --floor-dark: #8a6644;
    --title-blue: #3f95b8;
    --title-ink: #141414;
    --ball-light: #5fa9c9;
    --ball-mid: #3c7f93;
    --ball-dark: #25535c;
    --shadow: rgba(40, 24, 10, 0.55);
    --release: #f2ebe1;
    --year: #bfae9c;
  }
  html, body {
    margin: 0;
    padding: 0;
    width: 853px;
    height: 1200px;
    overflow: hidden;
    background: var(--wall-light);
  }
  .poster {
    position: relative;
    width: 853px;
    height: 1200px;
    overflow: hidden;
    background: radial-gradient(ellipse at 50% 30%, var(--wall-light) 0%, var(--wall-mid) 60%, var(--wall-edge) 100%);
  }
  .floor {
    position: absolute;
    left: 0;
    top: 762px;
    width: 853px;
    height: 438px;
    background: radial-gradient(ellipse at 50% 20%, var(--floor-light) 0%, var(--floor-mid) 55%, var(--floor-dark) 100%);
  }
  .title {
    position: absolute;
    left: 0;
    top: 0;
    width: 853px;
    height: 470px;
  }
  .title-main {
    font-family: "Montserrat", sans-serif;
    font-weight: 500;
    fill: var(--title-blue);
  }
  .title-sub {
    font-family: "Montserrat", sans-serif;
    font-weight: 100;
    fill: var(--title-ink);
  }
  .ball-shadow {
    position: absolute;
    left: 210px;
    top: 1000px;
    width: 420px;
    height: 110px;
    border-radius: 50%;
    background: radial-gradient(ellipse at center, var(--shadow) 0%, rgba(40,24,10,0.25) 50%, rgba(40,24,10,0) 75%);
  }
  .hero-ball {
    position: absolute;
    left: 137px;
    top: 512px;
    width: 550px;
    height: 550px;
    border-radius: 50%;
    background: radial-gradient(circle at 40% 25%, var(--ball-light) 0%, var(--ball-mid) 55%, var(--ball-dark) 100%);
  }
  .release {
    position: absolute;
    left: 0;
    width: 853px;
    text-align: center;
    margin: 0;
  }
  .release-label {
    top: 1045px;
    font-family: "Raleway", sans-serif;
    font-weight: 300;
    font-size: 34px;
    font-variant: small-caps;
    letter-spacing: 2px;
    color: var(--release);
  }
  .release-year {
    top: 1095px;
    font-family: "Arimo", sans-serif;
    font-weight: 700;
    font-size: 60px;
    letter-spacing: 1px;
    color: var(--year);
  }
</style>
</head>
<body>
  <main class="poster">
    <div class="floor"></div>

    <svg class="title" viewBox="0 0 853 470" xmlns="http://www.w3.org/2000/svg">
      <text class="title-main" x="125" y="261" font-size="298" textLength="608" lengthAdjust="spacingAndGlyphs">QUIET</text>
      <text class="title-sub" x="125" y="448" font-size="222" textLength="608" lengthAdjust="spacingAndGlyphs">FERNS</text>
    </svg>

    <div class="ball-shadow"></div>
    <div class="hero-ball" role="img" aria-label="Solid blue racquetball wearing a white sweatband with blue and red stripes, resting on the floor"></div>

    <p class="release release-label">Coming Soon</p>
    <p class="release release-year">2015</p>
  </main>
</body>
</html>
```